Banner Ad Design Project

Process description of accounting delivery A to Z

Your folder appointment for delivery of receipts, in and outgoing invoices not necessary but possible – goes into a industrial sized scanner at the office

Electronic delivery via email, NimbusBox or remote scanning locally at the clients office

Imported into the accounting software (called Arkivo) with drag and drop from email and NimbusBox our directly imported from scanner at clients office

Software sets ledger accounts after scanning largely automated
Imported into accounting softer and finished by producing Income statement , Balance sheet and cash flow statements.

Size should fit the www.fennivar.no webpage banners rolling

Target Market(s)

New Clients - its to sell our work as modern

Industry/Entity Type

Accounting

Requirements
Must have
• Color scheme fitting current webpage. Looking for a process driven illustration where details are more 1D not 3D as such. Simplified and easy to grasp scheme of flow in our production pipeline.

```html
<!DOCTYPE html>
<html lang="en">
<head>
<meta charset="utf-8">
<title>Fennivar – Standard &amp; Digital Delivery Process</title>
<link rel="stylesheet" href="https://fonts.googleapis.com/css2?family=Questrial&family=Barlow:wght@300&display=swap">
<style>
:root{
  --green:#208a6a;
  --green-text:#1f8a6a;
  --ink:#3a3a3a;
  --ink-soft:#555;
  --grey-top:#d9d9d9;
  --grey-bottom:#ececec;
  --panel:#ffffff;
  --rule:#b5b5b5;
  --badge:#e6e6e6;
}
*{margin:0;padding:0;box-sizing:border-box}
html,body{width:1200px;height:615px;overflow:hidden}
body{font-family:"Questrial",sans-serif;color:var(--ink);background:var(--grey-bottom)}
.stage{position:relative;width:1200px;height:615px;overflow:hidden}
.band-top{position:absolute;left:0;top:0;width:1200px;height:351px;background:var(--grey-top)}
.panel{position:absolute;left:145px;top:0;width:917px;height:605px;background:var(--panel)}
.navbar{position:absolute;left:164px;top:31px;width:879px;height:31px;background:var(--green)}
.nav-gap{position:absolute;left:199px;top:31px;width:120px;height:31px;background:var(--panel)}
.nav-links{position:absolute;left:371px;top:40px;display:flex;gap:14px;font-size:12px;color:#e8f3ef;list-style:none;white-space:nowrap}
.nav-links .current{color:#fff;font-weight:bold}
.lang{position:absolute;top:41px;width:15px;height:10px;background:#e9e9e9;border:1px solid #fff}
.logo{position:absolute;left:201px;top:16px;width:115px;height:115px;background:var(--green);color:#fff}
.logo-name{position:absolute;left:9px;top:78px;font-size:20px;letter-spacing:.2px;white-space:nowrap}
.logo-mark{position:absolute;left:80px;top:12px;width:22px;height:22px;background:#fff}
.title{position:absolute;left:0;width:1208px;top:90px;text-align:center;font-size:20px;font-weight:bold;color:#444;white-space:nowrap}
.step{position:absolute}
.step-num{position:absolute;left:0;top:0;width:21px;height:21px;border:2px solid #888;border-radius:50%;font-size:13px;color:#777;text-align:center;line-height:17px}
.step-head{position:absolute;left:27px;top:-1px;white-space:nowrap;font-size:17px;color:var(--ink)}
.step-sub{position:absolute;left:27px;top:18px;font-size:11.5px;color:var(--ink-soft);line-height:13.5px;width:220px}
.divider{position:absolute;top:151px;width:0;height:169px;border-left:2px dashed #bbb}
.phase-line{position:absolute;top:339px;border-top:2px dashed var(--rule)}
.phase-label{position:absolute;top:332px;font-size:12px;color:var(--ink-soft);white-space:nowrap}
.phase-arrow{position:absolute;top:329px}
.icon{position:absolute}
.brand-box{position:absolute;left:576px;top:189px;width:112px;height:31px;background:var(--green);color:#fff;font-size:20px;text-align:center;line-height:31px}
.cloud-name{position:absolute;left:306px;top:291px;font-size:16px;color:var(--ink);white-space:nowrap}
.remote-device{position:absolute;left:398px;top:281px;width:53px;height:34px;background:var(--green)}
.slogan{position:absolute;left:194px;top:418px;font-family:"Barlow",sans-serif;font-weight:300;font-size:34px;line-height:40.5px;color:var(--green-text);letter-spacing:.8px;white-space:nowrap}
.badge{position:absolute;background:var(--badge);border:1px solid #cfcfcf}
</style>
</head>
<body>
<div class="stage">
  <div class="band-top"></div>
  <div class="panel"></div>

  <div class="navbar"></div>
  <div class="nav-gap"></div>
  <ul class="nav-links">
    <li class="current">Home</li><li>About Fennivar</li><li>Accountant?</li><li>Services</li><li>Help &amp; Support</li>
  </ul>
  <span class="lang" style="left:991px"></span>
  <span class="lang" style="left:1009px"></span>

  <div class="logo"><span class="logo-mark"></span><span class="logo-name">fennivar</span></div>

  <h1 class="title">Standard &amp; Digital Delivery Process</h1>

  <!-- Delivery -->
  <div class="step" style="left:178px;top:149px">
    <span class="step-num">1</span>
    <p class="step-head">Scan incoming/outgoing receipts</p>
    <p class="step-sub">and prepare them for ledger entry</p>
  </div>
  <svg class="icon" style="left:258px;top:188px" width="140" height="44" viewBox="0 0 140 44" aria-label="Receipt plus scanner">
    <rect x="2" y="2" width="30" height="38" fill="none" stroke="#208a6a" stroke-width="2.5"/>
    <g stroke="#208a6a" stroke-width="2"><line x1="8" y1="10" x2="20" y2="10"/><line x1="8" y1="16" x2="20" y2="16"/><line x1="8" y1="22" x2="18" y2="22"/></g>
    <text x="21" y="34" font-size="10" fill="#208a6a" font-family="sans-serif" font-weight="bold">$</text>
    <path d="M42 24 l6 -6 l8 8 l6 -6" fill="none" stroke="#208a6a" stroke-width="3.5"/>
    <text x="74" y="30" font-size="16" font-weight="bold" fill="#333" font-family="sans-serif">+</text>
    <rect x="96" y="4" width="40" height="38" fill="#3a3a3a" role="img" aria-label="Document scanner"/>
  </svg>

  <div class="step" style="left:178px;top:241px">
    <span class="step-num">2</span>
    <p class="step-head">Client delivers them electronically</p>
    <p class="step-sub">via email, NimbusBox or remote scanning</p>
  </div>
  <svg class="icon" style="left:210px;top:286px" width="42" height="28" viewBox="0 0 42 28" aria-label="Email">
    <rect x="2" y="2" width="38" height="24" rx="3" fill="none" stroke="#208a6a" stroke-width="3.5"/>
    <path d="M4 5 L21 17 L38 5" fill="none" stroke="#208a6a" stroke-width="3.5"/>
  </svg>
  <svg class="icon" style="left:270px;top:290px" width="36" height="22" viewBox="0 0 36 22" aria-label="Cloud">
    <path d="M8 20 a7 7 0 0 1 0-13 a9 9 0 0 1 17-2 a7 7 0 0 1 3 15 z" fill="#3a3a3a"/>
  </svg>
  <span class="cloud-name">NimbusBox</span>
  <div class="remote-device" role="img" aria-label="Monitor and tablet for remote scanning"></div>

  <!-- Processing -->
  <div class="step" style="left:494px;top:149px">
    <span class="step-num">3</span>
    <p class="step-head">Import to accounting software</p>
    <p class="step-sub">directly from scanner or by drag and drop</p>
  </div>
  <div class="brand-box">Arkivo</div>

  <div class="step" style="left:494px;top:241px">
    <span class="step-num">4</span>
    <p class="step-head">The software creates ledger</p>
    <p class="step-sub">for each account</p>
  </div>
  <svg class="icon" style="left:576px;top:278px" width="120" height="46" viewBox="0 0 120 46" aria-label="Documents become a ledger">
    <rect x="1" y="1" width="28" height="36" fill="#fff" stroke="#333" stroke-width="2"/>
    <rect x="5" y="5" width="28" height="36" fill="#fff" stroke="#333" stroke-width="2"/>
    <rect x="9" y="9" width="28" height="36" fill="#fff" stroke="#333" stroke-width="2.5"/>
    <g stroke="#333" stroke-width="2"><line x1="14" y1="17" x2="32" y2="17"/><line x1="14" y1="23" x2="32" y2="23"/><line x1="14" y1="29" x2="32" y2="29"/><line x1="14" y1="35" x2="32" y2="35"/></g>
    <path d="M52 24 l6 6 l-6 6 M60 24 l6 6 l-6 6" fill="none" stroke="#208a6a" stroke-width="4"/>
    <path d="M80 3 h22 l8 8 v32 h-30 z" fill="none" stroke="#208a6a" stroke-width="2.5"/>
    <g stroke="#208a6a" stroke-width="2"><line x1="86" y1="14" x2="98" y2="14"/><line x1="86" y1="20" x2="104" y2="20"/></g>
    <circle cx="100" cy="35" r="6" fill="none" stroke="#208a6a" stroke-width="2"/>
  </svg>

  <!-- Finalization -->
  <div class="step" style="left:787px;top:149px">
    <span class="step-num">5</span>
    <p class="step-head">Generate reports</p>
    <p class="step-sub">Income statement, balance sheet and Cash flow statement</p>
  </div>
  <svg class="icon" style="left:882px;top:204px" width="130" height="46" viewBox="0 0 130 46" aria-label="Report documents">
    <path d="M2 2 h20 l8 8 v34 h-28 z" fill="none" stroke="#333" stroke-width="2"/>
    <g stroke="#333" stroke-width="1.5"><line x1="8" y1="18" x2="16" y2="18"/><line x1="8" y1="24" x2="24" y2="24"/><line x1="8" y1="30" x2="24" y2="30"/><line x1="8" y1="36" x2="24" y2="36"/></g>
    <rect x="46" y="2" width="32" height="42" fill="none" stroke="#208a6a" stroke-width="2"/>
    <g stroke="#208a6a" stroke-width="2"><rect x="51" y="8" width="8" height="6" fill="none"/><line x1="62" y1="10" x2="73" y2="10"/><line x1="51" y1="20" x2="73" y2="20"/><line x1="51" y1="26" x2="73" y2="26"/><line x1="51" y1="32" x2="73" y2="32"/><line x1="51" y1="38" x2="73" y2="38"/></g>
    <rect x="95" y="2" width="32" height="42" fill="none" stroke="#333" stroke-width="2.5"/>
    <g stroke="#333" stroke-width="2"><line x1="100" y1="10" x2="110" y2="10"/><line x1="100" y1="26" x2="122" y2="26"/><line x1="100" y1="32" x2="122" y2="32"/><line x1="100" y1="38" x2="122" y2="38"/></g>
    <text x="113" y="22" font-size="12" fill="#333" font-family="sans-serif">$</text>
  </svg>

  <!-- phase rules -->
  <span class="divider" style="left:477px"></span>
  <span class="divider" style="left:766px"></span>
  <span class="phase-line" style="left:183px;width:111px"></span>
  <span class="phase-label" style="left:306px">Delivery</span>
  <span class="phase-line" style="left:362px;width:100px"></span>
  <span class="phase-line" style="left:494px;width:88px"></span>
  <span class="phase-label" style="left:595px">Processing</span>
  <span class="phase-line" style="left:663px;width:88px"></span>
  <span class="phase-line" style="left:784px;width:76px"></span>
  <span class="phase-label" style="left:876px">Finalization</span>
  <span class="phase-line" style="left:948px;width:76px"></span>
  <svg class="phase-arrow" style="left:467px" width="21" height="21" viewBox="0 0 21 21" aria-label="Next phase">
    <circle cx="10.5" cy="10.5" r="9" fill="#fff" stroke="#bbb" stroke-width="2"/><path d="M5 10.5 h10 M11 6.5 l4 4 l-4 4" fill="none" stroke="#bbb" stroke-width="2"/>
  </svg>
  <svg class="phase-arrow" style="left:757px" width="21" height="21" viewBox="0 0 21 21" aria-label="Next phase">
    <circle cx="10.5" cy="10.5" r="9" fill="#fff" stroke="#bbb" stroke-width="2"/><path d="M5 10.5 h10 M11 6.5 l4 4 l-4 4" fill="none" stroke="#bbb" stroke-width="2"/>
  </svg>

  <p class="slogan">When you need an expert<br>with good business acumen<br>and local roots...</p>

  <span class="badge" style="left:857px;top:434px;width:62px;height:21px" role="img" aria-label="Professional association membership badge"></span>
  <span class="badge" style="left:932px;top:418px;width:73px;height:38px" role="img" aria-label="Financial supervisory authority badge"></span>
</div>
</body>
</html>
```